Business Card Design

I need a business card for my corporation. We are a fast food Mexican Taqueria located in San Jose, CA. I want the cards to include our business logo. The cards need to be simple but elegant. Our theme through out our locations is a beach feel atmosphere. I would like to see cards with a beach feeling. Our website is tacosdelpuerto.net and it would be great if the cards matched our website.

Industry/Entity Type

Business

Contact Information for Business Card

Monica Ferrer, VP
2637 Birch Hollow Ave
San Jose, CA 95116
Direct: 4085527319

```html
<!DOCTYPE html>
<html lang="en">
<head>
<meta charset="utf-8">
<title>Del Puerto Business Card</title>
<link rel="stylesheet" href="https://fonts.googleapis.com/css2?family=Cinzel:wght@400;700&family=Kaushan+Script&display=swap">
<style>
  :root {
    --page-bg: #3a2f3c;
    --sky-top: #5fa6dc;
    --sky-mid: #a9d3ef;
    --sea: #2f9fd0;
    --sea-light: #7ecbe8;
    --foam: #eef6f8;
    --sand: #ecd3ad;
    --sand-deep: #e2bf8f;
    --brand-red: #d0202c;
    --sun-yellow: #f5d318;
    --sign-paper: #f6efdc;
    --sign-wood: #9a7448;
    --rivet: #4a3b2c;
  }
  * { margin: 0; padding: 0; box-sizing: border-box; }
  html, body { width: 1200px; height: 800px; overflow: hidden; }
  body {
    background: var(--page-bg);
    display: flex;
    align-items: center;
    justify-content: center;
    gap: 60px;
    font-family: "Cinzel", serif;
  }
  .card {
    position: relative;
    width: 520px;
    height: 297px;
    border-radius: 4px;
    overflow: hidden;
    box-shadow: 0 14px 30px rgba(0,0,0,.45);
  }
  .beach-scene {
    position: absolute;
    inset: 0;
    background: linear-gradient(180deg,
      var(--sky-top) 0%, var(--sky-mid) 30%,
      var(--sea-light) 42%, var(--sea) 55%,
      var(--foam) 68%, var(--sand) 78%, var(--sand-deep) 100%);
  }
  /* Front: brand side */
  .card-front .brand {
    position: absolute;
    left: 46px;
    top: 64px;
    display: flex;
    align-items: center;
    gap: 14px;
  }
  .brand-name {
    font-family: "Cinzel", serif;
    font-weight: 700;
    font-size: 54px;
    color: var(--brand-red);
    line-height: 1;
  }
  .brand-sun {
    width: 34px;
    height: 34px;
    border-radius: 50%;
    background: var(--sun-yellow);
  }
  .tagline {
    position: absolute;
    left: 50px;
    top: 150px;
    font-size: 30px;
    color: var(--brand-red);
    letter-spacing: 1px;
  }
  .website {
    position: absolute;
    left: 50px;
    top: 204px;
    font-size: 22px;
    color: var(--brand-red);
    letter-spacing: .5px;
  }
  /* Back: contact side */
  .contact-sign {
    position: absolute;
    left: 92px;
    top: 40px;
    width: 350px;
    height: 200px;
    background: var(--sign-paper);
    border: 8px solid var(--sign-wood);
    box-shadow: 0 4px 10px rgba(0,0,0,.3);
    text-align: center;
    color: var(--brand-red);
    padding-top: 16px;
  }
  .rivet {
    position: absolute;
    width: 8px;
    height: 8px;
    border-radius: 50%;
    background: var(--rivet);
  }
  .rivet.tl { top: 6px; left: 6px; }
  .rivet.tr { top: 6px; right: 6px; }
  .rivet.bl { bottom: 6px; left: 6px; }
  .rivet.br { bottom: 6px; right: 6px; }
  .person-name {
    font-family: "Kaushan Script", cursive;
    font-size: 42px;
    line-height: 1.1;
  }
  .person-title {
    font-size: 22px;
    font-weight: 700;
    margin-bottom: 8px;
  }
  .contact-line {
    font-size: 16px;
    line-height: 1.35;
  }
  .contact-line.phone { font-size: 19px; }
</style>
</head>
<body>
  <section class="card card-front">
    <div class="beach-scene" role="img" aria-label="Photograph of a tropical beach with blue sky, ocean waves and sand"></div>
    <div class="brand">
      <span class="brand-name">Del Puerto</span>
      <span class="brand-sun"></span>
    </div>
    <p class="tagline">Sabor a México</p>
    <p class="website">www.tacosdelpuerto.net</p>
  </section>

  <section class="card card-back">
    <div class="beach-scene" role="img" aria-label="Photograph of a tropical beach with blue sky, ocean waves and sand"></div>
    <div class="contact-sign">
      <span class="rivet tl"></span><span class="rivet tr"></span>
      <span class="rivet bl"></span><span class="rivet br"></span>
      <p class="person-name">Monica Ferrer</p>
      <p class="person-title">VP</p>
      <p class="contact-line phone">Direct: 408-552-7319</p>
      <p class="contact-line">2637 Birch Hollow Ave</p>
      <p class="contact-line">San Jose CA 95116</p>
    </div>
  </section>
</body>
</html>
```